Website Design for Employee Moral and Happiness Company

Looking for a clean website design that explains our features in a step by step manner so our visitors know exactly what our site does before logging in.

The site is called "Velasto". See logo design and video for a sample of style and an overview of what we do.

Target Market(s)

Business owners that are looking to retain employees.

Number of Pages Required

1 page

```html
<!DOCTYPE html>
<html lang="en">
<head>
<meta charset="utf-8">
<title>Velasto</title>
<link href="https://fonts.googleapis.com/css2?family=Crimson+Text:wght@600;700&family=Nunito:wght@400;600;700&display=swap" rel="stylesheet">
<style>
  :root {
    --bg: #f2f2f2;
    --header-bg: #e8e0d7;
    --orange: #ff6600;
    --ink: #222222;
    --heading: #4a4a4a;
    --body: #5a5a5a;
    --line: #777777;
    --dot: #dddddd;
    --navy: #2b3a5a;
    --white: #ffffff;
  }
  * { margin: 0; padding: 0; box-sizing: border-box; }
  html, body { width: 1200px; height: 698px; overflow: hidden; background: var(--bg); }
  body { position: relative; font-family: "Nunito", sans-serif; color: var(--ink); }

  .site-header { position: absolute; left: 0; top: 0; width: 1200px; height: 89px; background: var(--header-bg); }
  .brand { position: absolute; left: 66px; top: 16px; font-family: "Crimson Text", serif; font-weight: 700; font-size: 42px; color: var(--ink); letter-spacing: 0.5px; }
  .main-nav a { position: absolute; top: 34px; font-size: 15px; color: #333; text-decoration: none; }
  .main-nav a.is-active { color: var(--orange); border-bottom: 1px solid var(--orange); }
  .login { position: absolute; left: 906px; top: 34px; font-size: 15px; color: #333; display: flex; align-items: center; gap: 9px; }
  .btn { position: absolute; background: var(--orange); color: var(--white); font-weight: 600; display: flex; align-items: center; justify-content: center; text-decoration: none; }
  .btn-header { left: 995px; top: 18px; width: 141px; height: 45px; border-radius: 23px; font-size: 15px; font-weight: 700; }
  .btn-cta { left: 66px; top: 575px; width: 245px; height: 52px; border-radius: 26px; font-size: 16px; }

  .dot-field { position: absolute; left: 852px; top: 98px; }

  .feature-art { position: absolute; top: 160px; height: 169px; }
  .art-rewards { left: 65px; width: 337px; background: linear-gradient(90deg, #e8e0d7 0%, #e8e0d7 8%, var(--navy) 14%, var(--navy) 48%, #e8e0d7 50%, var(--navy) 52%, var(--navy) 88%, #e8e0d7 94%, #e8e0d7 100%); }
  .art-transform { left: 427px; width: 340px; background: linear-gradient(135deg, #ff6a00, #e65c00); }

  .feature-title { position: absolute; top: 356px; font-family: "Crimson Text", serif; font-weight: 700; font-size: 21px; color: var(--heading); }
  .feature-text { position: absolute; top: 397px; width: 320px; font-size: 17px; line-height: 30px; color: var(--body); }

  .section-nav { position: absolute; left: 1160px; top: 255px; }
  .section-label { position: absolute; left: 1095px; top: 380px; font-size: 11px; line-height: 12px; color: var(--ink); }
</style>
</head>
<body>
  <header class="site-header">
    <div class="brand">velasto</div>
    <nav class="main-nav">
      <a class="is-active" style="left:278px">Home</a>
      <a style="left:342px">Boring Work Events</a>
      <a style="left:499px">Introducing Velasto</a>
      <a style="left:654px">Why Velasto</a>
      <a style="left:767px">Testimonials</a>
    </nav>
    <div class="login">
      <svg width="12" height="12" viewBox="0 0 12 12" fill="none" stroke="#333" stroke-width="1.2"><path d="M1 6h6M5 4l2 2-2 2M8 1h3v10H8"/></svg>
      Login
    </div>
    <a class="btn btn-header">SIGN UP</a>
  </header>

  <svg class="dot-field" width="348" height="240" aria-hidden="true">
    <defs><pattern id="dots" width="18.75" height="18.75" patternUnits="userSpaceOnUse"><circle cx="6" cy="6" r="2.2" fill="#dddddd"/></pattern></defs>
    <rect width="348" height="240" fill="url(#dots)"/>
  </svg>

  <div class="feature-art art-rewards" role="img" aria-label="Illustration of a ticket card and a bid paddle card"></div>
  <div class="feature-art art-transform" role="img" aria-label="Illustration of two photos, from a bored employee to a happy team"></div>

  <h3 class="feature-title" style="left:65px">3. Employee appreciation activities</h3>
  <p class="feature-text" style="left:76px">Lorem ipsum dolor sit amet, consectetur adipiscing elit, sed do eiusmod tempor incididunt ut labore accumsan lacus vel facilisis.</p>

  <h3 class="feature-title" style="left:434px">3. Transform Your Work Events</h3>
  <p class="feature-text" style="left:434px">Lorem ipsum dolor sit amet, consectetur adipiscing elit, sed do eiusmod tempor incididunt ut labore accumsan lacus vel facilisis.</p>

  <a class="btn btn-cta">SIGN UP&nbsp; NOW</a>

  <svg class="section-nav" width="30" height="280" viewBox="0 0 30 280" aria-hidden="true">
    <line x1="15" y1="15" x2="15" y2="263" stroke="#777777" stroke-width="1.5"/>
    <g fill="#f2f2f2" stroke="#777777" stroke-width="1.5">
      <circle cx="15" cy="15" r="5.6"/>
      <circle cx="15" cy="56" r="5.6"/>
      <circle cx="15" cy="97" r="5.6"/>
      <circle cx="15" cy="180" r="5.6"/>
      <circle cx="15" cy="221" r="5.6"/>
      <circle cx="15" cy="263" r="5.6"/>
    </g>
    <circle cx="15" cy="139" r="11" fill="#aaaaaa"/>
    <circle cx="15" cy="139" r="6" fill="#333333"/>
  </svg>
  <div class="section-label">Why choose<br>velasto</div>
</body>
</html>
```